CREATE R&B MIXTAPE COVER !!
Hi , my name is Brontel , and I want you to create a cover for my music mixtape.
The name of the mixtape is Tormenta , and has these types of music :
- R&B
- Hiphop
- Afrohouse
- Dancehall
- Reggaeton
In the attachments you’ll find two backgrounds. One with a lightning bolt , and a grey one with a stroke in the middle. I like both very much , but don’t know which one to choose. That’s why I want to compare the end results of both , and then make a decision. Below you’ll find instructions for both backgrounds.
If you think you can make something better for me , you can also try to do your own thing , and use your own background for example.
Instructions for the first background ( Lightning bolt )
I would like you to design my name ‘Brontel’ into / onto the lightning bolt. I want the lightning bolt + my name to be my DJ Logo , but my name doesn’t have to be in very big letters. Tormenta is the name of the mixtape and has to be in big letters. I was thinking above the logo.
Then there are 2 remaining sentences : ‘Mixed by DJ Brontel’ and ‘Mixtape Volume 1’. These two sentences have to be smaller than ‘Tormenta’. You can put them under the logo.
Instructions for the second background ( Grey )
I would like you to create a logo of my whole name ‘Brontel’ Or just with the letter V. You can put the logo above the stroke.
The mixtape name ‘Tormenta’ has to be in the middle in big letters.
Then there are 2 remaining sentences : ‘Mixed by DJ Brontel’ and ‘Mixtape Volume 1’. These two have to be smaller than ‘Tormenta’ in the middle. I want these sentences below.
Use your imagination with the name Tormenta , the two sentences and the logo. I want it to look professional and unique.
Kind regards ,
Brontel

```html
<!DOCTYPE html>
<html lang="en">
<head>
<meta charset="utf-8">
<title>Tormenta – Mixtape Volume 1</title>
<link rel="stylesheet" href="https://fonts.googleapis.com/css2?family=Metal+Mania&family=Open+Sans:wght@400;600;700&display=swap">
<style>
  :root {
    --bg-dark: #1c1d1f;
    --bg-mid: #2e3033;
    --band-light: #4a4d51;
    --glow-blue: #1fa8ff;
    --title-blue: #3fc8f2;
    --title-deep: #1a9fd6;
    --text-light: #f2f2f2;
    --logo-ice: #d8f3fc;
  }
  html, body {
    margin: 0;
    padding: 0;
    width: 1200px;
    height: 1200px;
    overflow: hidden;
    background: var(--bg-dark);
  }
  .cover {
    position: relative;
    width: 1200px;
    height: 1200px;
    overflow: hidden;
    background:
      repeating-linear-gradient(135deg, rgba(255,255,255,0.025) 0 2px, rgba(0,0,0,0.04) 2px 6px),
      radial-gradient(ellipse 70% 55% at 50% 40%, var(--bg-mid) 0%, var(--bg-dark) 75%, #141516 100%);
    font-family: "Open Sans", sans-serif;
  }
  .band {
    position: absolute;
    left: 0;
    top: 430px;
    width: 1200px;
    height: 260px;
    background:
      repeating-linear-gradient(135deg, rgba(255,255,255,0.03) 0 2px, rgba(0,0,0,0.05) 2px 6px),
      radial-gradient(ellipse 60% 90% at 50% 50%, var(--band-light) 0%, #35383b 55%, #26282a 100%);
    box-shadow: 0 0 40px rgba(0,0,0,0.6);
  }
  .glow-line {
    position: absolute;
    left: 50%;
    width: 900px;
    height: 4px;
    transform: translateX(-50%);
    background: radial-gradient(ellipse 50% 50% at 50% 50%, #bfeaff 0%, var(--glow-blue) 35%, rgba(31,168,255,0) 100%);
    box-shadow: 0 0 30px 8px rgba(31,168,255,0.35);
  }
  .glow-line.top { top: 428px; }
  .glow-line.bottom { top: 688px; }
  .glow-haze {
    position: absolute;
    left: 50%;
    width: 700px;
    height: 120px;
    transform: translateX(-50%);
    background: radial-gradient(ellipse 50% 50% at 50% 50%, rgba(31,168,255,0.28) 0%, rgba(31,168,255,0) 100%);
  }
  .glow-haze.top { top: 370px; }
  .glow-haze.bottom { top: 630px; }
  .brand {
    position: absolute;
    top: 120px;
    left: 0;
    width: 1200px;
    display: flex;
    flex-direction: column;
    align-items: center;
    gap: 22px;
  }
  .brand-dot {
    width: 22px;
    height: 22px;
    border-radius: 50%;
    background: var(--logo-ice);
  }
  .brand-name {
    margin: 0;
    font-weight: 700;
    font-size: 64px;
    letter-spacing: 10px;
    color: var(--logo-ice);
    line-height: 1;
  }
  .title {
    position: absolute;
    top: 480px;
    left: 0;
    width: 1200px;
    margin: 0;
    text-align: center;
    font-family: "Metal Mania", cursive;
    font-weight: 400;
    font-size: 178px;
    line-height: 1;
    letter-spacing: 6px;
    color: var(--title-blue);
    text-shadow: 0 0 18px rgba(31,168,255,0.45), 0 3px 0 var(--title-deep);
  }
  .credits {
    position: absolute;
    top: 1030px;
    left: 0;
    width: 1200px;
    text-align: center;
    color: var(--text-light);
  }
  .mixed-by {
    margin: 0;
    font-size: 38px;
    font-weight: 400;
    line-height: 1.2;
  }
  .volume {
    margin: 22px 0 0;
    font-size: 27px;
    font-weight: 400;
    letter-spacing: 9px;
    line-height: 1.2;
  }
</style>
</head>
<body>
  <main class="cover">
    <div class="band"></div>
    <div class="glow-haze top"></div>
    <div class="glow-haze bottom"></div>
    <div class="glow-line top"></div>
    <div class="glow-line bottom"></div>

    <header class="brand">
      <span class="brand-dot"></span>
      <p class="brand-name">BRONTEL</p>
    </header>

    <h1 class="title">TORMENTA</h1>

    <footer class="credits">
      <p class="mixed-by">Mixed by DJ Brontel</p>
      <p class="volume">Mixtape Volume 1</p>
    </footer>
  </main>
</body>
</html>
```